Cafe Menu for Willow Lantern Cafe

Menu designed for my cafe. I need multiple sizes to be created.
DL pamphlet
A4
and I also need 5 x A3 portraits & 5 x A3 landscapes. The menu must be spread out over a total of 10 A3 pages. I have uploaded my logo which needs to be used & I would like the colours from the logo used. The background of the menu needs to be white. I have uploaded an image on another menu for which I would like the same heading font to be used.

Target Market(s)

cafe, restaurant

Font styles to use
Serif
Decorative
Script

Requirements
Must have
• White back ground
correct font as I have uploaded
Nice to have
• May have drawings of food in back and white.

```html
<!DOCTYPE html>
<html lang="en">
<head>
<meta charset="utf-8">
<title>Willow Lantern Cafe – Menu</title>
<link href="https://fonts.googleapis.com/css2?family=Oswald:wght@300;400;500;600&family=Kaushan+Script&family=Reenie+Beanie&display=swap" rel="stylesheet">
<style>
:root{
  --ink:#1b1b1b;
  --soft-ink:#333333;
  --panel:#ffffff;
  --orange:#f2a11f;
  --green:#8db53a;
  --green-dark:#5f8a22;
  --white:#ffffff;
  --note:#f7e64a;
}
*{margin:0;padding:0;box-sizing:border-box}
html,body{width:1200px;height:849px;overflow:hidden;background:var(--white)}
body{position:relative;font-family:"Oswald",sans-serif;color:var(--ink)}
.page{position:absolute;top:37px;width:550px;height:777px;background:var(--panel);overflow:hidden;box-shadow:0 0 3px rgba(0,0,0,.4)}
.page--drinks{left:33px}
.page--food{left:616px}
.layer{position:absolute;left:0;top:0}
.brand{position:absolute;left:23px;top:-3px;width:126px;height:126px;border-radius:50%;background:var(--white);border:4px solid var(--green);color:var(--ink);text-align:center;padding-top:30px}
.brand__name{font-size:13px;font-weight:400;color:var(--green-dark);line-height:1.1}
.brand__tag{font-size:9.5px;font-weight:300;margin-top:6px}
.brand__addr{font-size:6px;font-weight:300;margin-top:12px;line-height:1.3}
.brand__phone{font-size:7px;font-weight:300}
.menu-badge{position:absolute;left:224px;top:44px;width:104px;height:53px;background:var(--green);display:flex;align-items:center;justify-content:center}
.menu-badge span{font-family:"Kaushan Script",cursive;font-size:44px;color:#111;line-height:1;margin-top:-2px}
.col{position:absolute}
.section{position:absolute;left:0;right:0}
.heading{display:block;background:var(--orange);color:var(--white);font-weight:500;font-size:11.5px;letter-spacing:.3px;line-height:16px;height:16px;padding-left:5px;width:118px;margin-bottom:3px}
.heading--plain{background:none;color:var(--ink);padding-left:0;font-size:12px}
.item{font-size:10.5px;line-height:14px}
.item__row{display:flex;justify-content:space-between;font-weight:500}
.item__desc{font-weight:300;font-size:9.3px;line-height:13.3px;color:var(--soft-ink)}
.food .item{line-height:13.4px;margin-bottom:8.5px}
.food .item__desc{line-height:13.2px}
.rule{height:1.6px;background:var(--orange);margin-top:4px}
.art{position:absolute;border-radius:6px}
.note{position:absolute;left:280px;top:636px;width:72px;height:66px;background:var(--note);transform:rotate(-12deg);color:#222;font-family:"Reenie Beanie",cursive;font-size:12px;line-height:12px;text-align:center;padding-top:13px;box-shadow:1px 2px 2px rgba(0,0,0,.3)}
.info{position:absolute;left:330px;width:220px;top:660px;text-align:center;color:#1a1a1a;font-size:9px;line-height:12.6px;font-weight:400}
.info__name{font-weight:600;font-size:11.5px;margin-top:8px;letter-spacing:.3px}
.info__addr{font-size:9px}
</style>
</head>
<body>

<section class="page page--drinks">
  <svg class="layer" width="550" height="777" viewBox="0 0 550 777">
    <defs>
      <linearGradient id="warmPhoto" x1="0" y1="0" x2="1" y2="1">
        <stop offset="0" stop-color="#e9a54a"/><stop offset=".5" stop-color="#efe1c8"/><stop offset="1" stop-color="#c99a5e"/>
      </linearGradient>
      <linearGradient id="burgerPhoto" x1="0" y1="0" x2="1" y2="1">
        <stop offset="0" stop-color="#c98a3c"/><stop offset=".6" stop-color="#8a5a2b"/><stop offset="1" stop-color="#d9b07a"/>
      </linearGradient>
      <linearGradient id="paniniPhoto" x1="0" y1="0" x2="1" y2="0">
        <stop offset="0" stop-color="#e4b34f"/><stop offset="1" stop-color="#c98a3c"/>
      </linearGradient>
    </defs>
    <g role="img" aria-label="Photo of a breakfast plate with fruit and fried egg">
      <rect x="0" y="0" width="430" height="99" fill="url(#warmPhoto)"/>
    </g>
    <g role="img" aria-label="Photo of a burger, fries and pastries">
      <polygon points="407,0 550,0 550,152 428,131" fill="url(#burgerPhoto)"/>
    </g>
    <polygon points="0,98 430,98 430,103 0,103" fill="var(--green)"/>
    <polyline points="407,0 428,131 550,152" fill="none" stroke="var(--green)" stroke-width="5"/>
    <path d="M276,700 L300,690 C330,680 350,660 380,650 C420,640 470,640 550,630 L550,777 L276,777 Z" fill="var(--green)"/>
    <g role="img" aria-label="Photo of a toasted panini with fruit">
      <polygon points="150,777 170,752 220,740 276,742 276,777" fill="url(#paniniPhoto)"/>
    </g>
  </svg>

  <div class="brand">
    <div class="brand__name">Willow Lantern Cafe</div>
    <div class="brand__tag">Coffee, breakfast &amp; lunch</div>
    <div class="brand__addr">14 Harlow Street, Brindle Q</div>
    <div class="brand__phone">Phone: 07 5550 1842</div>
  </div>

  <div class="menu-badge"><span>Menu</span></div>

  <div class="art" style="left:150px;top:262px;width:80px;height:52px;background:#e58a3a" role="img" aria-label="Illustration of colourful iced drinks"></div>
  <div class="art" style="left:205px;top:392px;width:36px;height:44px;background:#e9a6c4" role="img" aria-label="Illustration of a berry smoothie"></div>
  <div class="art" style="left:205px;top:548px;width:32px;height:56px;background:#f1c6d3" role="img" aria-label="Illustration of a milkshake"></div>
  <div class="art" style="left:417px;top:144px;width:55px;height:50px;background:#b46a3c" role="img" aria-label="Illustration of a hot coffee cup"></div>
  <div class="art" style="left:472px;top:306px;width:31px;height:42px;background:#c58d55" role="img" aria-label="Illustration of a takeaway coffee cup"></div>
  <div class="art" style="left:451px;top:466px;width:42px;height:52px;background:#d9a86a" role="img" aria-label="Illustration of a child eating breakfast"></div>

  <div class="col" style="left:22px;width:248px;top:0">
    <div class="section" style="top:137px">
      <div class="heading">COLD DRINKS</div>
      <div style="padding-left:6px">
        <div class="item"><div class="item__row"><span>Milkshake</span><span>$7.00</span></div></div>
        <div class="item"><div class="item__row"><span>Thickshake</span><span>$8.00</span></div>
          <div class="item__desc">Flavours - Chocolate, vanilla, strawberry, banana,<br>caramel &amp; coffee</div></div>
        <div class="item"><div class="item__row"><span>Iced Latte</span><span>$7.50</span></div>
          <div class="item__desc">Add syrup: vanilla, caramel, white chocolate,<br>hazelnut</div></div>
        <div class="item"><div class="item__row"><span>Iced Coffee</span><span>$8.00</span></div></div>
        <div class="item"><div class="item__row"><span>Iced Chocolate</span><span>$8.00</span></div></div>
        <div class="item"><div class="item__row"><span>Iced Mocha</span><span>$8.00</span></div></div>
      </div>
      <div class="rule" style="width:227px"></div>
    </div>
    <div class="section" style="top:312px">
      <div class="heading">JUICE BAR</div>
      <div style="padding-left:6px">
        <div class="item"><div class="item__row"><span>Passion Pop</span><span>$9.00</span></div>
          <div class="item__desc">Passionfruit, apple &amp; oranges</div></div>
        <div class="item"><div class="item__row"><span>Sweet Juice</span><span>$9.00</span></div>
          <div class="item__desc">Apple, pineapple, oranges &amp; mango</div></div>
        <div class="item"><div class="item__row"><span>Orange Juice</span><span>$9.00</span></div>
          <div class="item__desc">Freshly juiced oranges</div></div>
      </div>
      <div class="rule" style="width:200px"></div>
    </div>
    <div class="section" style="top:426px">
      <div class="heading">SMOOTHIES</div>
      <div style="padding-left:6px">
        <div class="item"><div class="item__row"><span>Mango Raspberry Smoothie</span><span>$9.00</span></div>
          <div class="item__desc">Frozen mango &amp; raspberry sorbet blended<br>with coconut milk</div></div>
        <div class="item"><div class="item__row"><span>Mango Coconut Smoothie</span><span>$9.00</span></div>
          <div class="item__desc">Frozen mango blended with coconut milk</div></div>
        <div class="item"><div class="item__row"><span>Berry Blast Smoothie</span><span>$9.00</span></div>
          <div class="item__desc">Mixed berries blended with coconut milk</div></div>
        <div class="item"><div class="item__row"><span>Choc Banana Smoothie $9.00</span><span></span></div>
          <div class="item__desc">Frozen banana &amp; dark chocolate ice cream<br>blended together with whole milk</div></div>
      </div>
      <div class="rule" style="width:200px"></div>
    </div>
    <div class="section" style="top:602px">
      <div class="heading">FRAPPES</div>
      <div style="padding-left:6px">
        <div class="item"><div class="item__row"><span>Strawberry Lemonade Frappe</span><span>$9.00</span></div>
          <div class="item__desc">Strawberry syrup blended together with<br>lemonade &amp; ice</div></div>
        <div class="item"><div class="item__row"><span>Coffee Frappe</span><span>$9.00</span></div>
          <div class="item__desc">Espresso blended with milk &amp; ice, topped with<br>cream</div></div>
        <div class="item"><div class="item__row"><span>Chocolate Frappe</span><span>$9.00</span></div>
          <div class="item__desc">Chocolate syrup blended with milk &amp; ice, topped<br>with cream</div></div>
      </div>
    </div>
  </div>

  <div class="col" style="left:290px;width:233px;top:0">
    <div class="section" style="top:111px"><div class="heading">COFEE MENU</div></div>
    <div class="section" style="top:135px">
      <div class="heading">COFFEE &amp; HOT DRINKS</div>
      <div style="padding-left:1px">
        <div class="item"><div class="item__row"><span>Cappuccino</span><span>$4.80</span></div></div>
        <div class="item"><div class="item__row"><span>Flat White</span><span>$4.80</span></div></div>
        <div class="item"><div class="item__row"><span>Latte</span><span>$5.00</span></div></div>
        <div class="item"><div class="item__row"><span>Long Black</span><span>$4.80</span></div></div>
        <div class="item"><div class="item__row"><span>Mocha</span><span>$5.20</span></div></div>
        <div class="item"><div class="item__row"><span>Macchiato</span><span>$3.50</span></div></div>
        <div class="item"><div class="item__row"><span>Espresso</span><span>$3.50</span></div></div>
        <div class="item"><div class="item__row"><span>Chai Latte</span><span>$4.80</span></div></div>
        <div class="item"><div class="item__row"><span>Hot Chocolate</span><span>$4.80</span></div></div>
        <div class="item"><div class="item__row"><span>Tea</span><span>$4.50</span></div>
          <div class="item__desc">Tea Flavours: English breakfast, earl grey,<br>green, berry green &amp; coconut</div></div>
      </div>
      <div class="rule" style="width:180px"></div>
    </div>
    <div class="section" style="top:340px">
      <div class="heading">TAKEAWAY COFFEE</div>
      <div style="padding-left:1px">
        <div class="item"><div class="item__row"><span>Takeaway Large</span><span>$6.80</span></div></div>
        <div class="item"><div class="item__row"><span>Takeaway Regular</span><span>$5.20</span></div></div>
        <div class="item"><div class="item__row"><span>Takeaway Small</span><span>$4.80</span></div></div>
      </div>
      <div class="rule" style="width:220px"></div>
    </div>
    <div class="section" style="top:412px">
      <div class="heading">COFFEE EXTRAS</div>
      <div style="padding-left:1px">
        <div class="item"><div class="item__row"><span>Mug &amp; Extra Shot</span><span style="width:24px">50c</span></div></div>
        <div class="item"><div class="item__row"><span>Soy &amp; Lactose Free Milk</span><span style="width:24px">80c</span></div></div>
        <div class="item"><div class="item__row"><span>Syrups</span><span>$1.00</span></div></div>
      </div>
      <div class="rule" style="width:160px"></div>
    </div>
    <div class="section" style="top:488px">
      <div class="heading">KIDS MENI</div>
      <div style="padding-left:1px">
        <div class="item"><div class="item__row"><span>Scrambled Eggs -</span><span>$9.50</span></div>
          <div class="item__desc">Two eggs scrambled with toast &amp; tomato<br>sauce</div></div>
        <div class="item"><div class="item__row"><span>Rainbow Pancakes -</span><span>$9.50</span></div>
          <div class="item__desc">Two small pancakes served with ice cream<br>&amp; sprinkles</div></div>
        <div class="item"><div class="item__row"><span>Nuggets &amp; Chips -</span><span>$8.00</span></div></div>
        <div class="item"><div class="item__row"><span>Chicken Chippees -</span><span>$8.50</span></div></div>
      </div>
    </div>
  </div>

  <div class="note">Phone Orders<br>Welcome!<br>07 5550 1842</div>

  <div class="info">
    <div>Open 7 Days From 7am</div>
    <div>Open Weekends</div>
    <div>Saturday &amp; Sunday 7am-12pm</div>
    <div>Menu Online: www.willowlanterncafe.com.au</div>
    <div>Email: hello@willowlanterncafe.com.au</div>
    <div>10% Surcharge Applies on Sundays &amp; Public Holidays</div>
    <div class="info__name">Willow Lantern Cafe</div>
    <div class="info__addr">14 Harlow Street, Brindle Q 4721</div>
  </div>
</section>

<section class="page page--food food">
  <svg class="layer" width="550" height="777" viewBox="0 0 550 777">
    <defs>
      <linearGradient id="breakfastStrip" x1="0" y1="0" x2="1" y2="0">
        <stop offset="0" stop-color="#d9a45c"/><stop offset=".35" stop-color="#eae4da"/><stop offset=".7" stop-color="#9fb0a8"/><stop offset=".85" stop-color="#9cc04a"/><stop offset="1" stop-color="#d8d2c8"/>
      </linearGradient>
    </defs>
    <g role="img" aria-label="Photo strip of pancakes, fried eggs and breakfast dishes">
      <rect x="0" y="0" width="550" height="40" fill="url(#breakfastStrip)"/>
    </g>
    <rect x="0" y="40" width="550" height="4" fill="var(--green)"/>
    <path d="M0,735 C150,765 350,776 550,772 L550,777 L0,777 Z" fill="var(--green)"/>
  </svg>

  <div class="col" style="left:20px;width:248px;top:53px">
    <div class="heading" style="margin-bottom:5px">BREAK FAST MENU</div>
    <div style="padding-left:4px">
      <div class="item"><div class="item__row"><span>Big Breakfast</span><span>$21.50</span></div>
        <div class="item__desc">Bacon, sausages, hash browns, tomato,<br>baked beans &amp; mushrooms with a slice of toasted<br>panini bread &amp; your choice of fried,poached or<br>scrambled eggs.</div></div>
      <div class="item"><div class="item__row"><span>Classic Breakfast</span><span>$16.50</span></div>
        <div class="item__desc">Your choice of fried poached or scrambled eggs<br>served with either bacon or sausages, tomato &amp; a<br>slice of panini toast</div></div>
      <div class="item"><div class="item__row"><span>Avocado Stack</span><span>$17.00</span></div>
        <div class="item__desc">Turkish bread topped with avocado, bacon or salmon,<br>2 poached eggs &amp; a sprinkle of feta cheese</div></div>
      <div class="item"><div class="item__row"><span>Eggs Benedict</span><span>$19.00</span></div>
        <div class="item__desc">Your choice of bacon, ham or salmon served with<br>toasted turkish bread, poached eggs &amp; creamy<br>hollandaise sauce</div></div>
      <div class="item"><div class="item__row"><span>Classic Omelet</span><span>$17.50</span></div>
        <div class="item__desc">Ham, tomato, spinach, onion &amp; cheese omelet topped<br>with fried cherry tomatoes &amp; turkish toast</div></div>
      <div class="item"><div class="item__row"><span>Panini Scramble</span><span>$16.50</span></div>
        <div class="item__desc">Toasted panini bread topped with scrambled eggs,<br>sautéed mushrooms, cherry tomatoes &amp; spinach with<br>a drizzle of hollandaise sauce on top</div></div>
      <div class="item"><div class="item__row"><span>Breaky Wrap</span><span>$15.00</span></div>
        <div class="item__desc">Bacon, eggs, hash browns, cheese &amp; BBQ sauce on a<br>toasted wrap</div></div>
      <div class="item"><div class="item__row"><span>Ultimate Breakfast Toastie</span><span>$14.50</span></div>
        <div class="item__desc">Bacon, scrambled eggs, smashed avocado, spinach &amp;<br>feta with hollandaise sauce on a toasted ciabatta<br>sandwich roll</div></div>
      <div class="item"><div class="item__row"><span>Breakfast Share Plate</span><span>$28.50</span></div>
        <div class="item__desc">A delicious selection of yummy breakfast items including<br>bacon, scrambled eggs, hash browns, croissant, yogurt,<br>strawberries &amp; blueberries.</div></div>
      <div class="item"><div class="item__row"><span>Fruity Pancakes</span><span>$17.50</span></div>
        <div class="item__desc">3 fluffy pancakes topped with a tropical fruit mix<br>&nbsp;including strawberries, mango &amp; blueberries with a<br>sprinkle of icing sugar, served with maple syrup.</div></div>
      <div class="item"><div class="item__row"><span>Bacon Avocado Salsa</span><span>$17.50</span></div>
        <div class="item__desc">Smashed avocado topped with diced tomato &amp; bacon<br>with spinach, a sprinkle of feta, a side of hash browns<br>&nbsp;&amp; a wedge of lemon</div></div>
    </div>
  </div>

  <div class="col" style="left:279px;width:248px;top:53px">
    <div class="heading" style="margin-bottom:5px">LUNCH MENU</div>
    <div style="padding-left:3px">
      <div class="item"><div class="item__row"><span>Parmi Turkish Roll</span><span>$16.50</span></div>
        <div class="item__desc">Chicken tenders, tomato relish, cheese, lettuce<br>&amp; herb mayo served on a toasted turkish roll with a<br>side of chips</div></div>
      <div class="item"><div class="item__row"><span>Sweet Potato Chips</span><span>$13.50</span></div>
        <div class="item__desc">Seasoned sweet potato chips served with a herb mayonnaise</div></div>
      <div class="item"><div class="item__row"><span>Chicken Avocado Panini Grill</span><span>$15.50</span></div>
        <div class="item__desc">Chicken, avocado, cheese &amp; aioli served on toasted<br>panini bread &amp; grilled with a side of chips</div></div>
      <div class="item"><div class="item__row"><span>Steak Sandwich</span><span>$17.50</span></div>
        <div class="item__desc">Fillet steak with salad, cheese &amp; BBQ sauce on<br>toasted bread with a side of chips</div></div>
      <div class="item"><div class="item__row"><span>Club Sandwich</span><span>$16.50</span></div>
        <div class="item__desc">Three slices of toasted bread with ham, bacon,<br>chicken, tomato, cheese, lettuce &amp; mayonnaise<br>with a side of chips</div></div>
      <div class="item"><div class="item__row"><span>Fresh or Toasted Sandwich</span><span>$8.00</span></div>
        <div class="item__desc">Your choice of meat, salad &amp; sauce on fresh white or<br>wholemeal bread toasted or fresh</div></div>
      <div class="item"><div class="item__row"><span>Pulled Pork Turkish Roll -</span><span>$15.50</span></div>
        <div class="item__desc">Pulled pork mixed with gravy, house made coleslaw,<br>lettuce &amp; herb mayonnaise on a toasted turkish roll<br>with a side of chips</div></div>
      <div class="item" style="margin-bottom:1px"><div class="item__row"><span>Fish, Chips &amp; Salad -</span><span>$17.50</span></div>
        <div class="item__desc">Battered fillets with chips &amp; salad, herb mayonnaise,<br>lemon &amp; salad dressing.</div></div>
      <div class="item" style="margin-bottom:1px"><div class="item__row"><span>Nachos -</span><span>$16.50</span></div>
        <div class="item__desc">Nacho chips topped with nacho mince, cheese sauce,<br>melted cheese, diced tomato &amp; smashed avocado.</div></div>
      <div class="item" style="margin-bottom:18px"><div class="item__row"><span>Lunch Bruschetta</span><span>$16.50</span></div>
        <div class="item__desc">Toasted sourdough bread with avocado, cherry<br>tomatoes, onion, feta &amp; a drizzle of balsamic glaze with<br>a side of chips</div></div>
      <div class="heading heading--plain" style="margin-bottom:2px">SALADS</div>
      <div class="item"><div class="item__row"><span>Caesar Salad</span><span>$16.50</span></div>
        <div class="item__desc">Chicken breast with lettuce, bacon, egg, parmesan cheese,<br>croutons &amp; caesar dressing</div></div>
      <div class="item"><div class="item__row"><span>Mango Chicken Salad</span><span>$16.50</span></div>
        <div class="item__desc">Chicken breast, lettuce, mango, onion &amp; cashews with a<br>creamy curry dressing</div></div>
      <div class="item"><div class="item__row"><span>Tropical Prawn Salad -</span><span>$17.50</span></div>
        <div class="item__desc">Cooked prawns with avocado, tomato, cucumber and<br>mango salsa mixed through with mixed lettuce and poppyseed<br>dressing.</div></div>
    </div>
  </div>
</section>

</body>
</html>
```